Supplement Bottle Label Design and Creative Lifestyle Images

We are a medical home consumer brand and we are releasing a supplement line of products called "Velbrook Nutrition". We are in need of a supplement bottle design for our supplement line, Velbrook Nutrition. We are looking for a very appealing, simple, and clean design, but with a medical feel to it.

We would like to see designs with a black background as well as designs with a white background. Bottle size will approximately be 200cc and label will about be 7" x 2.5", but this size is subject to change.

We really like the Pirlen Nutrition design and the Gantry Lab, however, we like the medical style of Nutrition Keystones. Please reference the links below.

To start off, the title of this bottle will be "Calm-Spire". We will need all similar warning about FDA, made in USA, non-GMA, GMP, ect. Please use the formula below to start:

2 Pills per serving
Blueberry pterostilbene - 10mg
Bacopa - 150mg
Gingko Biloba - 50mg
Vinpocetine - 10mg
Alpha-GPC -150mg
TAU - 35mg

https://www.shopvarn.example/Pirlen-Nutrition/b/ref=bl_dp_s_web_48213907562?ie=UTF8&node=48213907562&field-lbr_brands_browse-bin=Pirlen+Nutrition

https://www.shopvarn.example/l/7394208156

https://www.shopvarn.example/Nutrition-Keystones/b/ref=bl_dp_s_web_86420531977?ie=UTF8&node=86420531977&field-lbr_brands_browse-bin=Nutrition+Keystones

Industry/Entity Type

Medical

```html
<!DOCTYPE html>
<html lang="en">
<head>
<meta charset="utf-8">
<title>Velbrook Nutrition – CalmSpire Label</title>
<link rel="stylesheet" href="https://fonts.googleapis.com/css2?family=Lato:wght@300;400;700;900&display=swap">
<style>
  :root {
    --page: #eef0f1;
    --label-black: #0c0d0e;
    --label-edge: #1c1f21;
    --teal: #3fb7b2;
    --teal-band: #3a8f8c;
    --teal-deep: #1f5f5d;
    --teal-light: #6fd6d0;
    --ink-soft: #c9cfd1;
    --ink-white: #f2f4f4;
  }
  * { box-sizing: border-box; margin: 0; padding: 0; }
  html, body {
    width: 1200px;
    height: 2168px;
    overflow: hidden;
  }
  body {
    background: var(--page);
    font-family: "Lato", sans-serif;
    position: relative;
  }
  .label {
    position: absolute;
    left: 80px;
    top: 184px;
    width: 1040px;
    height: 1800px;
    background: linear-gradient(90deg, var(--label-black) 0%, var(--label-edge) 50%, var(--label-black) 100%);
    border-radius: 18px;
    overflow: hidden;
  }
  .brand {
    position: absolute;
    top: 190px;
    left: 0;
    width: 100%;
    display: flex;
    justify-content: center;
    align-items: center;
    gap: 22px;
  }
  .brand-dot {
    width: 46px;
    height: 46px;
    border-radius: 50%;
    background: var(--teal);
  }
  .brand-name {
    color: var(--teal);
    font-weight: 700;
    font-size: 68px;
    letter-spacing: 0.5px;
  }
  .claim {
    position: absolute;
    top: 380px;
    left: 0;
    width: 100%;
    text-align: center;
    color: var(--ink-soft);
    font-weight: 300;
    font-size: 54px;
    line-height: 74px;
    letter-spacing: 1px;
    text-transform: uppercase;
  }
  .name-band {
    position: absolute;
    top: 1030px;
    left: 0;
    width: 100%;
    height: 230px;
    background: var(--teal-band);
    display: flex;
    justify-content: center;
    align-items: center;
  }
  .product-name {
    font-size: 178px;
    line-height: 1;
    letter-spacing: -2px;
  }
  .product-name .light { color: var(--teal-deep); font-weight: 300; }
  .product-name .bold { color: var(--teal-light); font-weight: 900; }
  .supplement-type {
    position: absolute;
    top: 1340px;
    left: 0;
    width: 100%;
    text-align: center;
    color: var(--ink-white);
    font-weight: 400;
    font-size: 50px;
    letter-spacing: 1px;
  }
  .volume {
    position: absolute;
    top: 1600px;
    left: 0;
    width: 100%;
    text-align: center;
    color: var(--teal);
    font-weight: 400;
    font-size: 34px;
  }
</style>
</head>
<body>
  <main class="label">
    <header class="brand">
      <span class="brand-dot"></span>
      <span class="brand-name">Velbrook Nutrition</span>
    </header>
    <p class="claim">For<br>A Better Memory<br>More Focus &amp;<br>Clarity</p>
    <section class="name-band">
      <h1 class="product-name"><span class="light">Calm</span><span class="bold">Spire</span></h1>
    </section>
    <p class="supplement-type">DIETARY SUPPLEMENT</p>
    <p class="volume">200cc</p>
  </main>
</body>
</html>
```